I need a business card.

I need a simple, minimalist, business card. I think the coolest business card I have ever seen is Marty Vexler's from Brimstone Heist... it is just a little creepy for the real world.
I am a photographer and I need a card that I can give to brides or potential portrait customers that is simple and classy.
My name is Gil Anstrade. My website is www.gilanstrade-example.com
Please design my card.
I think it could be as simple as my name, phone # and website... where the rest of my contact could be found... or maybe my email and no website... I am open to ideas. I imagined the card on thick card stock with a black background...

```html
<!DOCTYPE html>
<html lang="en">
<head>
<meta charset="utf-8">
<title>Gil Anstrade Photography – Business Card</title>
<link rel="stylesheet" href="https://fonts.googleapis.com/css2?family=Arimo:wght@700&display=swap">
<style>
  :root {
    --page-bg: #a9a9a9;
    --card-light: #8a8a8a;
    --card-mid: #3a3a3a;
    --card-dark: #000000;
    --ink: #ffffff;
    --ink-shadow: rgba(0, 0, 0, 0.75);
  }
  * { margin: 0; padding: 0; box-sizing: border-box; }
  html, body {
    width: 1200px;
    height: 1200px;
    overflow: hidden;
    background: var(--page-bg);
  }
  .sheet {
    position: relative;
    width: 1200px;
    height: 1200px;
  }
  .card {
    position: absolute;
    left: 198px;
    width: 772px;
    height: 486px;
    overflow: hidden;
    font-family: "Arimo", Arial, sans-serif;
    font-weight: 700;
    color: var(--ink);
  }
  .card--front { top: 66px; }
  .card--back { top: 618px; }
  .card__surface {
    position: absolute;
    inset: 0;
    background:
      radial-gradient(ellipse 70% 85% at 38% 42%, var(--card-light) 0%, var(--card-mid) 55%, rgba(0,0,0,0) 100%),
      linear-gradient(90deg, #2a2a2a 0%, #1a1a1a 70%, var(--card-dark) 100%);
  }
  .brand {
    position: absolute;
    left: 0;
    right: 0;
    top: 150px;
    display: flex;
    flex-direction: column;
    align-items: center;
  }
  .brand__block {
    display: flex;
    flex-direction: column;
    align-items: flex-end;
  }
  .brand__name {
    font-size: 70px;
    line-height: 1;
    letter-spacing: 0.12em;
    margin-right: -0.12em;
    text-shadow: 2px 3px 5px var(--ink-shadow);
  }
  .brand__tag {
    margin-top: 6px;
    font-size: 19px;
    letter-spacing: 0.16em;
    margin-right: -0.16em;
    text-shadow: 1px 2px 3px var(--ink-shadow);
  }
  .contact {
    position: absolute;
    left: 0;
    right: 0;
    text-align: center;
    text-shadow: 2px 3px 5px var(--ink-shadow);
  }
  .contact__web {
    top: 138px;
    font-size: 32px;
    letter-spacing: 0.1em;
  }
  .contact__phone {
    top: 296px;
    font-size: 31px;
    letter-spacing: 0.12em;
  }
</style>
</head>
<body>
  <main class="sheet">
    <section class="card card--front" aria-label="Card front">
      <div class="card__surface" role="img" aria-label="Dark fine-mesh texture, lit softly from the centre"></div>
      <div class="brand">
        <div class="brand__block">
          <h1 class="brand__name">GIL ANSTRADE</h1>
          <p class="brand__tag">PHOTOGRAPHY</p>
        </div>
      </div>
    </section>

    <section class="card card--back" aria-label="Card back">
      <div class="card__surface" role="img" aria-label="Dark fine-mesh texture, lit softly from the centre"></div>
      <p class="contact contact__web">www.gilanstrade-example.com</p>
      <p class="contact contact__phone">555 014 2276</p>
    </section>
  </main>
</body>
</html>
```